Mirela Hastow ADHD coach needs a flyer

I need a flyer to be sent by email. the copy is attached. It can be changed/reduced to fit the flyer. I would like to keep my website colors. My website is www.mirelahastow.example - Thank you!

```html
<!DOCTYPE html>
<html lang="en">
<head>
<meta charset="utf-8">
<title>Mirela Hastow – ADHD and Academic Coach</title>
<link href="https://fonts.googleapis.com/css2?family=Encode+Sans+Semi+Condensed:wght@400&family=Fira+Sans+Condensed:wght@500;600&family=Open+Sans:ital,wght@0,300;0,400;0,700;1,400&family=Cormorant+SC:wght@500&family=Cardo:ital@1&family=Source+Sans+3:wght@300;400&display=swap" rel="stylesheet">
<style>
:root{
  --bg:#e7eaeb;
  --slate:#5e6f6b;
  --muted:#a9b6b6;
  --teal-green:#3b8b7b;
  --blue:#0aafe1;
  --blue-soft:#74cfe0;
  --ice:#c6ecf8;
  --blush:#fbe3ef;
  --grey-band:#95a4a4;
  --text:#3f4646;
  --soft-text:#6b7373;
  --orange:#f5892a;
  --tick:#5fc4dc;
}
*{margin:0;padding:0;box-sizing:border-box}
html,body{width:1200px;height:2234px;overflow:hidden;background:#fff}
.flyer{position:relative;width:1200px;height:2234px;background:linear-gradient(90deg,#eceeef 0%,#e4e7e8 100%);font-family:"Open Sans",sans-serif;color:var(--text);overflow:hidden}
.abs{position:absolute}
.top-bar{left:0;top:40px;width:1200px;height:60px;background:#f3f4f4;text-align:center;font:400 30px/60px "Source Sans 3",sans-serif;color:#8d9a9a;letter-spacing:.5px}
.portrait{left:560px;top:100px;width:640px;height:1105px;background:linear-gradient(180deg,#dfe5e7 0%,#eed9dd 45%,#f3dfe3 70%,#dde3e5 100%)}
.name{left:36px;top:160px;font:400 110px/1 "Encode Sans Semi Condensed",sans-serif;color:var(--slate);letter-spacing:-2px;text-shadow:2px 2px 0 #c8d0cf}
.credential{left:134px;top:290px;font:500 27px/1 "Cormorant SC",serif;color:var(--muted);letter-spacing:1px}
.headline{left:22px;top:412px;width:720px;font:500 35px/40px "Fira Sans Condensed",sans-serif;color:var(--teal-green)}
.banner{left:0;top:503px;width:620px;height:180px}
.banner-text{left:23px;top:522px;width:540px;font:700 23px/27.5px "Open Sans",sans-serif;color:#fff}
.intro-box{left:5px;top:690px;width:967px;height:397px;background:rgba(255,255,255,.88);border-radius:10px;padding:18px 24px 0 24px;display:flex;gap:24px}
.intro-box .col{width:446px;font:400 18.5px/27.6px "Open Sans",sans-serif;color:#3b3f3f;text-align:justify}
.intro-box p+p{margin-top:27.6px}
.focus-pill{left:27px;top:1145px;width:593px;height:58px;background:var(--blue);border-radius:12px;color:#fff;display:flex;align-items:center;padding-left:36px}
.focus-pill .label{font:600 31px "Fira Sans Condensed",sans-serif}
.focus-pill .sub{font:italic 33px "Cardo",serif;margin-left:14px}
.focus-pill svg{position:absolute;left:12px;top:19px}
.focus-intro{left:71px;top:1212px;width:510px;font:300 17px/28px "Open Sans",sans-serif;color:var(--soft-text)}
.help-list{left:59px;top:1307px;width:537px}
.help-item{position:relative;height:68px;margin-bottom:11px;padding:0 10px 0 68px;display:flex;align-items:center;font:300 17px/21px "Open Sans",sans-serif;color:#4d5555}
.help-item:nth-child(odd){background:var(--ice)}
.help-item:nth-child(even){background:var(--blush)}
.help-item svg{position:absolute;left:20px;top:10px}
.voices{left:44px;top:1778px;width:569px;height:412px;background:#e4e8ea;text-align:center;padding:16px 30px 0}
.voices h3{font:400 29px/36px "Source Sans 3",sans-serif;color:var(--blue)}
.voices blockquote{font:italic 400 15.5px/21.5px "Open Sans",sans-serif;color:#3d4343;margin:2px 0 20px}
.outcomes{left:650px;top:1113px;width:450px;height:697px;background:#fff;box-shadow:2px 2px 0 #d6dcdd;padding:26px 20px 0 32px}
.outcomes .tri{position:absolute;right:14px;top:16px}
.outcomes h2{font:600 31px/34px "Fira Sans Condensed",sans-serif;color:var(--blue)}
.outcomes h4{font:italic 600 26px/26px "Fira Sans Condensed",sans-serif;color:#3a4040;margin-top:2px}
.outcomes ul{list-style:none;margin-top:16px}
.outcomes li{position:relative;padding-left:38px;font:400 18.5px/34.5px "Open Sans",sans-serif;color:#4a5050;letter-spacing:.4px}
.outcomes li svg{position:absolute;left:0;top:7px}
.outcomes h2.second{margin-top:14px}
.next-band{left:648px;top:1840px;width:410px;height:81px}
.next-title{left:666px;top:1843px;font:500 58px/74px "Fira Sans Condensed",sans-serif;color:#fff}
.contact{left:662px;top:1932px;width:430px;font:400 30px/31px "Source Sans 3",sans-serif;color:#96a2a2}
.contact .call{padding-left:96px;margin-top:6px}
.contact .line{display:flex;align-items:center;color:var(--blue);font-size:33px;margin-top:8px}
.contact .line svg{margin-right:8px}
.contact .phone{padding-left:54px}
.contact .mail{padding-left:52px}
.bottom-bar{left:0;top:2197px;width:1200px;height:37px;background:#9aa6a6}
</style>
</head>
<body>
<div class="flyer">
  <div class="abs top-bar">www.mirelahastow.example</div>

  <div class="abs portrait" role="img" aria-label="Portrait photograph of the coach in a pale pink blazer, arms crossed, against a light wall"></div>

  <h1 class="abs name">MIRELA HASTOW</h1>
  <div class="abs credential">Ph.D. &nbsp;|&nbsp; ADHD and Academic Coach</div>

  <h2 class="abs headline">Helping Your Child with ADHD or Other Learning Challenges Thrive in College and Beyond</h2>

  <svg class="abs banner" width="620" height="180" viewBox="0 0 620 180" aria-hidden="true">
    <polygon points="0,25 612,25 550,180 0,180" fill="var(--blue-soft)"/>
    <polygon points="0,0 585,0 522,160 0,160" fill="var(--blue)"/>
  </svg>
  <p class="abs banner-text">Academic success coaching that leads to lifelong transformation for students with ADHD and similar challenges that may have impeded their ability to thrive.</p>

  <section class="abs intro-box">
    <div class="col">
      <p>Sending your child off to college can feel scary, especially if that college is hundreds of miles away. You worry about how they'll do on their own—whether they'll make friends, earn good grades, and be happy—especially without you there to support them daily. You know your child is bright, and you want them to have a great future, but you're concerned they will struggle without the right support and resources.</p>
      <p>You don't need to feel helpless as you send your child off to this next stage of their lives. Mirela is dedicated to making that transition easier for</p>
    </div>
    <div class="col">
      <p>everyone. Mirela Hastow has years of experience helping students thrive despite their challenges. She sees your child's potential and helps them see it, too. She provides a safety net as they adjust to a new environment at college.</p>
      <p>Her services are comprehensive and adaptable, based on the requirements of each individual: helping with course selection and scheduling, time management, study strategies, focus, making new friends, and adapting to change. Through it all, Mirela guides students through fundamental work on mind set to ensure that changes stick.</p>
    </div>
  </section>

  <div class="abs focus-pill">
    <svg width="12" height="20" viewBox="0 0 12 20" aria-hidden="true"><polygon points="0,0 12,10 0,20" fill="var(--orange)"/></svg>
    <span class="label">Empowering Focus:</span><span class="sub">How Mirela Helps</span>
  </div>
  <p class="abs focus-intro">Mirela has taken students from failing to a 3.0 GPA, and from a C student to the Dean's List, in just one semester. It doesn't take years to provide lasting results; all it takes is the right guide.</p>

  <div class="abs help-list">
    <div class="help-item"><svg width="30" height="50" viewBox="0 0 30 50" aria-hidden="true"><polygon points="0,0 30,25 0,50" fill="#87928f"/></svg>Uniquely positioned to help your child, Mirela: Tailors support so that your child improves focus and maximizes their potential in college and beyond.</div>
    <div class="help-item"><svg width="30" height="50" viewBox="0 0 30 50" aria-hidden="true"><polygon points="0,0 30,25 0,50" fill="#87928f"/></svg>Understands your child's unique needs - she sees the gifts that others often miss.</div>
    <div class="help-item"><svg width="30" height="50" viewBox="0 0 30 50" aria-hidden="true"><polygon points="0,0 30,25 0,50" fill="#87928f"/></svg>Knows the academic landscape intimately, including the challenges faced by students with ADHD and other conditions.</div>
    <div class="help-item"><svg width="30" height="50" viewBox="0 0 30 50" aria-hidden="true"><polygon points="0,0 30,25 0,50" fill="#87928f"/></svg>Helps with the logistics of scheduling in a way that most advisors can't, enrolling students in the courses that best suit their learning style.</div>
    <div class="help-item"><svg width="30" height="50" viewBox="0 0 30 50" aria-hidden="true"><polygon points="0,0 30,25 0,50" fill="#87928f"/></svg>Nurtures the brilliance in your bright child.</div>
    <div class="help-item"><svg width="30" height="50" viewBox="0 0 30 50" aria-hidden="true"><polygon points="0,0 30,25 0,50" fill="#87928f"/></svg>Provides a balance between encouraging students and challenging them.</div>
  </div>

  <section class="abs voices">
    <h3>What Parents Say</h3>
    <blockquote>“Mirela was the glue that kept our daughter in college... as our daughter's Academic Coach, [she] gave our daughter the ability to finish strong by empowering her with the skills needed to be successful.”—Lorna</blockquote>
    <blockquote>“Mirela has always told my daughter not that she can succeed, but that she will succeed.”—Beatrix</blockquote>
    <h3>What Students Say</h3>
    <blockquote>“Last semester I completed all 16 hours and I had the highest GPA I've ever had!” —Former student</blockquote>
    <blockquote>“Under her instruction, my grades began to improve. I ended up making the Dean's List during my time at Halvern, and I was also inducted into Theta Kappa Rho. I am currently in my first year of law school at Westbrook University, a top tier school.”—Former student</blockquote>
  </section>

  <section class="abs outcomes">
    <svg class="tri" width="24" height="14" viewBox="0 0 24 14" aria-hidden="true"><polygon points="0,0 24,0 12,14" fill="var(--orange)"/></svg>
    <h2>Realizing Potential:</h2>
    <h4>The Transformation<br>You'll See in Your Child</h4>
    <ul>
      <li><svg width="22" height="22" viewBox="0 0 22 22" aria-hidden="true"><circle cx="11" cy="11" r="10" fill="none" stroke="var(--tick)" stroke-width="2"/><circle cx="11" cy="11" r="7" fill="var(--tick)"/><path d="M7 11l3 3 5-6" fill="none" stroke="#fff" stroke-width="2"/></svg>A mindset of self-belief and increased confidence.</li>
      <li><svg width="22" height="22" viewBox="0 0 22 22" aria-hidden="true"><circle cx="11" cy="11" r="10" fill="none" stroke="var(--tick)" stroke-width="2"/><circle cx="11" cy="11" r="7" fill="var(--tick)"/><path d="M7 11l3 3 5-6" fill="none" stroke="#fff" stroke-width="2"/></svg>Higher grades and the drive to graduate.</li>
      <li><svg width="22" height="22" viewBox="0 0 22 22" aria-hidden="true"><circle cx="11" cy="11" r="10" fill="none" stroke="var(--tick)" stroke-width="2"/><circle cx="11" cy="11" r="7" fill="var(--tick)"/><path d="M7 11l3 3 5-6" fill="none" stroke="#fff" stroke-width="2"/></svg>Social integration and making friends.</li>
      <li><svg width="22" height="22" viewBox="0 0 22 22" aria-hidden="true"><circle cx="11" cy="11" r="10" fill="none" stroke="var(--tick)" stroke-width="2"/><circle cx="11" cy="11" r="7" fill="var(--tick)"/><path d="M7 11l3 3 5-6" fill="none" stroke="#fff" stroke-width="2"/></svg>Happiness and fulfilment.</li>
      <li><svg width="22" height="22" viewBox="0 0 22 22" aria-hidden="true"><circle cx="11" cy="11" r="10" fill="none" stroke="var(--tick)" stroke-width="2"/><circle cx="11" cy="11" r="7" fill="var(--tick)"/><path d="M7 11l3 3 5-6" fill="none" stroke="#fff" stroke-width="2"/></svg>A deep sense of personal achievement and pride.</li>
    </ul>
    <h2 class="second">You Will Have:</h2>
    <ul>
      <li><svg width="22" height="22" viewBox="0 0 22 22" aria-hidden="true"><circle cx="11" cy="11" r="10" fill="none" stroke="var(--tick)" stroke-width="2"/><circle cx="11" cy="11" r="7" fill="var(--tick)"/><path d="M7 11l3 3 5-6" fill="none" stroke="#fff" stroke-width="2"/></svg>Less stress, knowing that your child is in good hands.</li>
      <li><svg width="22" height="22" viewBox="0 0 22 22" aria-hidden="true"><circle cx="11" cy="11" r="10" fill="none" stroke="var(--tick)" stroke-width="2"/><circle cx="11" cy="11" r="7" fill="var(--tick)"/><path d="M7 11l3 3 5-6" fill="none" stroke="#fff" stroke-width="2"/></svg>Fewer sleepless nights worrying about your child.</li>
      <li><svg width="22" height="22" viewBox="0 0 22 22" aria-hidden="true"><circle cx="11" cy="11" r="10" fill="none" stroke="var(--tick)" stroke-width="2"/><circle cx="11" cy="11" r="7" fill="var(--tick)"/><path d="M7 11l3 3 5-6" fill="none" stroke="#fff" stroke-width="2"/></svg>Confidence that they are receiving the right support.</li>
      <li><svg width="22" height="22" viewBox="0 0 22 22" aria-hidden="true"><circle cx="11" cy="11" r="10" fill="none" stroke="var(--tick)" stroke-width="2"/><circle cx="11" cy="11" r="7" fill="var(--tick)"/><path d="M7 11l3 3 5-6" fill="none" stroke="#fff" stroke-width="2"/></svg>Joy and pride at seeing them do well.</li>
    </ul>
  </section>

  <svg class="abs next-band" width="410" height="81" viewBox="0 0 410 81" aria-hidden="true"><polygon points="0,0 410,0 370,81 0,81" fill="var(--grey-band)"/></svg>
  <h2 class="abs next-title">Next Steps</h2>

  <div class="abs contact">
    <p>To learn more and discuss<br>your child's individual needs,</p>
    <p class="call">call:</p>
    <p class="line phone"><svg width="30" height="40" viewBox="0 0 30 40" aria-hidden="true"><rect x="6" y="2" width="17" height="34" rx="3" transform="rotate(-12 15 19)" fill="none" stroke="var(--blue)" stroke-width="2"/></svg>555·018·4420</p>
    <p class="call">or, email:</p>
    <p class="line mail"><svg width="34" height="26" viewBox="0 0 34 26" aria-hidden="true"><rect x="2" y="3" width="30" height="20" fill="none" stroke="var(--blue)" stroke-width="2"/><path d="M2 3l15 12 15-12M2 23l11-10M32 23l-11-10" fill="none" stroke="var(--blue)" stroke-width="2"/></svg>coach@mirelahastow.example</p>
  </div>

  <div class="abs bottom-bar"></div>
</div>
</body>
</html>
```